Flyer-Design zum Thema Bewertungsportale DIN lang(9,8 x 21 cm)
Zielgruppe
Zahnklinik mit allen Fachrichtungen
Aufgabenstellung
Modernes und pfiffiges Design, bitte an unserem Corporate-Design orientieren. Generell arbeiten wir in unseren Designs viel mit den Kreisen, welche als Datei beigefügt sind. Die Kreise sind oft in Ecken angeschnitten, mal größer mal kleiner. In dem Fall würde ich 3 verschiedene Farben an Kreisen nehmen, grün muss auf jeden Fall dabei sein. evtl. kann man auch ein schönes Bild bei bildquelle-xq.de vorschlagen, was zum Thema Bewertungsportale passt. Zum Beispiel so etwas: https://de.bildquelle-xq.com/id/574203918 oder https://de.bildquelle-xq.com/id/562917034 , ich lasse gerade den Text erstellen. Bitte solange Platzhalter verwenden, 4 Absätze, oben eine Begrüßung, Erklärung und dann 3 Absätze mit jeweils einer kurzerklärung zum jeweiligen bewertungsportal. 1. Suchlix, 2. praxiwert , 3. freundnetz am ende ganz unten einen dankessatz. wie gesagt texte kommen noch bitte schonmal Grafiken setzen und schönen Flyer gestalten mit Platzhaltern. auf der Rückseite sollten unsere 3 Labels genannt werden Sonnenblick Praxis, Sonnenblick Spange, Sonnenblick Kinderpraxis
vielleicht kann man auch den Einleitungstext auf die Rückseite drauf machen.
Das ist der Text für den Flyer:
Sie sind mit uns zufrieden? Sagen Sie es weiter!
Wir haben Sie fachmännisch behandelt. Wir sind auf Ihre Wünsche und Ängste eingegangen. Atmosphäre und Kommunikation in unserer Praxis stimmen. Sie gehen zufrieden nach Hause und kommen auch das nächste Mal wieder mit einem guten Gefühl zu uns.
Das freut uns sehr. Noch mehr freuen wir uns, wenn Sie uns im Netz bewerten – damit auch online ein richtiges Bild davon entsteht, was wir bei Sonnenblick Praxis jeden Tag für unsere Patienten leisten.
Deshalb möchten wir Sie hiermit bitten: Machen Sie Ihre gute Meinung über uns öffentlich. Jede positive Rezension bei Suchlix, Praxiwert oder Freundnetz zählt.
So bewerten Sie uns bei Suchlix
Geben Sie „Sonnen Blick Praxis' in das Suchlix-Suchfeld ein. Links erscheint die Liste der Suchergebnisse, rechts eine Zusam..

```html
<!DOCTYPE html>
<html lang="de">
<head>
<meta charset="utf-8">
<title>Flyer Bewertungsportale – Sonnenblick Praxis</title>
<link href="https://fonts.googleapis.com/css2?family=Encode+Sans+Semi+Condensed:wght@300;600&display=swap" rel="stylesheet">
<style>
  :root {
    --stage: #b3b3b3;
    --paper: #ffffff;
    --ink: #3a3a3a;
    --green: #b4cd14;
    --green-soft: #e3eab2;
    --blue: #4aa8dd;
    --blue-soft: #c6e2f3;
    --purple: #5b2d8e;
    --social-red: #dd4b39;
    --social-teal: #3aa7c9;
    --social-navy: #3b5998;
  }
  * { box-sizing: border-box; margin: 0; padding: 0; }
  html, body { width: 849px; height: 1200px; overflow: hidden; }
  body {
    background: var(--stage);
    font-family: "Encode Sans Semi Condensed", sans-serif;
    font-weight: 300;
    color: var(--ink);
    position: relative;
  }
  .flyer {
    position: absolute;
    top: 182px;
    width: 390px;
    height: 836px;
    background: var(--paper);
    overflow: hidden;
    box-shadow: 4px 6px 10px rgba(0,0,0,0.25);
  }
  .flyer--front { left: 20px; }
  .flyer--back { left: 440px; }

  .flyer__header { height: 68px; position: relative; }
  .brand {
    position: absolute;
    right: 26px;
    top: 18px;
    text-align: right;
    color: var(--green);
  }
  .brand__name { font-size: 20px; line-height: 1; }
  .brand__claim { font-size: 7px; color: var(--ink); margin-top: 3px; }

  .label-row {
    display: flex;
    justify-content: space-between;
    align-items: flex-start;
    padding: 26px 24px 0;
  }
  .label { font-size: 9.5px; line-height: 1; }
  .label small { display: block; font-size: 3.6px; color: var(--ink); margin-top: 2px; }
  .label--praxis { color: var(--green); }
  .label--spange { color: var(--blue); }
  .label--kinder { color: var(--purple); }

  .photo { height: 312px; width: 100%; }
  .photo--rating {
    background: linear-gradient(180deg, #dcdcdc 0%, #f2f2f2 35%, #ffffff 55%, #ececec 100%);
  }
  .photo--family {
    background: linear-gradient(180deg, #e6eef4 0%, #d8c4b0 45%, #e9d8a8 60%, #6b7895 100%);
  }

  .content { position: relative; z-index: 2; padding: 0 27px 0 24px; }
  .headline {
    font-weight: 600;
    color: var(--green);
    font-size: 25px;
    line-height: 30px;
    margin-top: 20px;
  }
  .copy {
    font-size: 12.6px;
    line-height: 16.8px;
    text-align: justify;
    hyphens: auto;
  }
  .copy + .copy { margin-top: 16px; }
  .front-copy { margin-top: 22px; }
  .thanks { margin-top: 26px; font-size: 12.6px; line-height: 16.8px; }

  .portal + .portal { margin-top: 12px; }
  .portal__title {
    font-weight: 600;
    font-size: 13.5px;
    line-height: 17px;
  }
  .portal--search .portal__title { color: var(--green); }
  .portal--rating .portal__title { color: var(--blue); }
  .portal--social .portal__title { color: var(--purple); }
  .portal__note { font-size: 8.6px; line-height: 11px; }
  .back-content { padding-top: 24px; }

  .deco { position: absolute; left: 0; top: 0; z-index: 1; }

  .footer {
    position: absolute;
    left: 24px;
    right: 0;
    top: 782px;
    z-index: 3;
    display: flex;
    align-items: center;
  }
  .socials { display: flex; gap: 6px; }
  .social { width: 18px; height: 18px; border-radius: 50%; }
  .social--a { background: var(--social-red); }
  .social--b { background: var(--social-teal); }
  .social--c { background: var(--social-navy); }
  .web {
    margin-left: 56px;
    font-weight: 600;
    font-size: 13.5px;
  }
  .flyer--front .web { color: var(--green); }
  .flyer--back .web { color: var(--blue); }
</style>
</head>
<body>

  <section class="flyer flyer--front">
    <header class="flyer__header">
      <div class="brand">
        <div class="brand__name">Sonnenblick Praxis</div>
        <div class="brand__claim">Gesunde Zähne, gutes Gefühl</div>
      </div>
    </header>
    <div class="photo photo--rating" role="img" aria-label="Foto: Finger tippt auf fünf leuchtende blaue Bewertungssterne vor hellem Raum"></div>

    <svg class="deco" width="390" height="836" aria-hidden="true">
      <circle cx="349" cy="810" r="141" fill="var(--green-soft)"/>
      <circle cx="347" cy="790" r="26" fill="none" stroke="var(--green)" stroke-width="11"/>
    </svg>

    <div class="content">
      <h1 class="headline">Sie sind mit uns zufrieden?<br>Sagen Sie es weiter!</h1>
      <p class="copy front-copy">Wir haben Sie fachmännisch behandelt. Wir sind auf Ihre Wünsche und Ängste eingegangen. Atmosphäre und Kommunikation in unserer Praxis stimmen. Sie gehen zufrieden nach Hause und kommen auch das nächste Mal wieder mit einem guten Gefühl zu uns. Das freut uns sehr.</p>
      <p class="copy">Noch mehr freuen wir uns, wenn Sie uns im Netz bewerten – damit auch online ein richtiges Bild davon entsteht, was wir bei Sonnenblick Praxis jeden Tag für unsere Patienten leisten. Deshalb möchten wir Sie hiermit bitten: Machen Sie Ihre gute Meinung über uns öffentlich. Jede positive Rezension bei Suchlix, Praxiwert oder Freundnetz zählt.</p>
      <p class="thanks">Ganz herzlichen Dank für Ihre Bewertung(en)<br>und bis zum nächsten Termin!<br>Wir freuen uns auf Sie! Ihr Sonnenblick Team Lindenfeld</p>
    </div>

    <footer class="footer">
      <div class="socials"><span class="social social--a"></span><span class="social social--b"></span><span class="social social--c"></span></div>
      <span class="web">www.sonnenblickpraxis.de</span>
    </footer>
  </section>

  <section class="flyer flyer--back">
    <header class="flyer__header">
      <div class="label-row">
        <div class="label label--praxis">Sonnenblick Praxis<small>Gesunde Zähne, gutes Gefühl</small></div>
        <div class="label label--spange">Sonnenblick Spange<small>Kieferorthopädie für Kinder, Jugendliche und Erwachsene</small></div>
        <div class="label label--kinder">Sonnenblick Kinderpraxis<small>Zahnärztl. Gemeinschaftspraxis für Kinder &amp; Jugendliche</small></div>
      </div>
    </header>
    <div class="photo photo--family" role="img" aria-label="Foto: lachende Familie mit zwei Kindern am sonnigen Strand"></div>

    <svg class="deco" width="390" height="836" aria-hidden="true">
      <circle cx="349" cy="810" r="141" fill="var(--blue-soft)"/>
      <circle cx="347" cy="790" r="26" fill="none" stroke="var(--blue)" stroke-width="11"/>
    </svg>

    <div class="content back-content">
      <div class="portal portal--search">
        <h2 class="portal__title">So bewerten Sie uns bei Suchlix</h2>
        <p class="copy">Geben Sie «Sonnen Blick Praxis» in das Suchlix-Suchfeld ein. Links erscheint die Liste der Suchergebnisse, rechts eine Zusammenfassung von Informationen zu unserer Praxis. Klicken sie auf den neben den Bewertungssternen erscheinenden Linktext «Suchlix-Rezensionen», dann auf «Rezension schreiben». Jetzt können Sie Ihre Sternchen hinterlassen – schön wäre es auch, wenn Sie noch einen kleinen Text schreiben.</p>
      </div>
      <div class="portal portal--rating">
        <h2 class="portal__title">So bewerten Sie uns bei Praxiwert</h2>
        <p class="copy">Auf Deutschlands größtem Arztempfehlungsportal praxiwert.de finden Sie uns, indem Sie «mvz sonnenblick praxis» ins Suchfenster eingeben. Bei unserem Profil angelangt, klicken Sie auf «Zahnärzte bewerten». Jetzt suchen Sie in der Liste Ihren Behandler und hinterlassen Ihr detailliertes Feedback.</p>
      </div>
      <div class="portal portal--social">
        <h2 class="portal__title">So bewerten Sie uns bei Freundnetz</h2>
        <p class="copy">Suchen Sie bei www.freundnetz.de nach sonnenblick praxis. Jetzt können Sie sofort loslegen: Einfach bei «Bewertungen» Sternchen markieren und Bewertungstext eingeben.</p>
        <p class="portal__note">(Das funktioniert nur, wenn Sie Freundnetz-Mitglied und eingeloggt sind.)</p>
      </div>
    </div>

    <footer class="footer">
      <div class="socials"><span class="social social--a"></span><span class="social social--b"></span><span class="social social--c"></span></div>
      <span class="web">www.sonnenblickpraxis.de</span>
    </footer>
  </section>

</body>
</html>
```